New Business Card Design Project

Hi! I would like for you to design a business card for our aesthetic injections business. We offer Zelvia, filler, skin care. I would like it to be elegant, feminine, modern and sleek/clean. I like black/gold foil/ivory/parchment colors. It can be either one or two sided. I would like matte black with gold foil logo on one side and ivory with gold foil information on the other side

Target Market(s)

target market is the discerning woman who wants to look her best

Industry/Entity Type

beauty

Contact Information for Business Card

logo, name, phone, email, website, instagram, facebook, location

Requirements
Must have
• logo and info
Nice to have
• the icons for cell, instagram, email, fb etc
Should not have
• images of people

```html
<!DOCTYPE html>
<html lang="en">
<head>
<meta charset="utf-8">
<title>The Velvet Atelier — Business Card</title>
<link href="https://fonts.googleapis.com/css2?family=Montserrat:wght@400;500;700&display=swap" rel="stylesheet">
<style>
  :root {
    --backdrop: #1c1c1d;
    --card-black: #1f1f20;
    --card-ivory: #f8f6dc;
    --gold: #c9a23a;
    --gold-light: #f0d878;
    --gold-deep: #a87f1e;
    --ink: #141414;
  }
  * { box-sizing: border-box; margin: 0; padding: 0; }
  html, body { width: 1200px; height: 1015px; overflow: hidden; }
  body {
    background: var(--backdrop);
    font-family: "Montserrat", Arial, sans-serif;
    display: flex;
    flex-direction: column;
    align-items: center;
    justify-content: center;
    gap: 60px;
  }
  .card {
    width: 700px;
    height: 400px;
    position: relative;
    overflow: hidden;
    box-shadow: 0 12px 30px rgba(0,0,0,.55);
  }
  .card-front {
    background: var(--card-black);
    display: flex;
    align-items: center;
    justify-content: center;
  }
  .front-brand {
    font-size: 92px;
    font-weight: 500;
    letter-spacing: 6px;
    color: var(--gold);
  }
  .card-back { background: var(--card-ivory); }
  .foil-band {
    position: absolute;
    left: 175px;
    width: 92px;
    background: linear-gradient(135deg, var(--gold-deep), var(--gold-light) 45%, var(--gold) 70%, var(--gold-deep));
  }
  .foil-band.top { top: 0; height: 70px; }
  .foil-band.bottom { bottom: 0; height: 70px; }
  .brand-seal {
    position: absolute;
    left: 81px;
    top: 60px;
    width: 280px;
    height: 280px;
    border-radius: 50%;
    border: 1.5px solid var(--gold);
    background: var(--card-ivory);
    display: flex;
    align-items: center;
    justify-content: center;
    text-align: center;
  }
  .seal-name {
    font-size: 24px;
    font-weight: 500;
    letter-spacing: 4px;
    line-height: 1.5;
    color: var(--gold);
  }
  .contact {
    position: absolute;
    left: 410px;
    top: 70px;
    color: var(--ink);
  }
  .person-name {
    font-size: 24px;
    font-weight: 700;
    letter-spacing: 1px;
    color: var(--gold);
  }
  .person-role { font-size: 15px; margin-top: 2px; }
  .contact-list { list-style: none; margin-top: 28px; font-size: 15px; line-height: 1.6; }
  .contact-list li { display: flex; align-items: center; gap: 8px; }
  .contact-list svg { width: 14px; height: 14px; fill: var(--gold); flex: none; }
  .address { margin-top: 28px; font-size: 15px; line-height: 1.4; }
</style>
</head>
<body>
  <section class="card card-front">
    <span class="front-brand">Velvet</span>
  </section>

  <section class="card card-back">
    <div class="foil-band top"></div>
    <div class="foil-band bottom"></div>
    <div class="brand-seal">
      <span class="seal-name">THE<br>VELVET<br>ATELIER</span>
    </div>

    <div class="contact">
      <p class="person-name">MARCUS HALE</p>
      <p class="person-role">Managing Director</p>
      <ul class="contact-list">
        <li>
          <svg viewBox="0 0 24 24" aria-hidden="true"><path d="M6.6 10.8a15.1 15.1 0 0 0 6.6 6.6l2.2-2.2a1 1 0 0 1 1-.25 11.4 11.4 0 0 0 3.6.57 1 1 0 0 1 1 1V20a1 1 0 0 1-1 1A17 17 0 0 1 3 4a1 1 0 0 1 1-1h3.5a1 1 0 0 1 1 1c0 1.25.2 2.45.57 3.57a1 1 0 0 1-.25 1z"/></svg>
          044-987 650 312
        </li>
        <li>
          <svg viewBox="0 0 24 24" aria-hidden="true"><path d="M2 5h20v14H2zm2 2v.5l8 5 8-5V7l-8 5z"/></svg>
          hello@velvetatelier.com
        </li>
        <li>
          <svg viewBox="0 0 24 24" aria-hidden="true"><path d="M12 2a10 10 0 1 0 0 20 10 10 0 0 0 0-20zm6.9 6h-2.9a15.7 15.7 0 0 0-1.4-3.6A8 8 0 0 1 18.9 8zM12 4c.8 1.2 1.5 2.5 1.9 4h-3.8c.4-1.5 1.1-2.8 1.9-4zM4.3 14a8 8 0 0 1 0-4h3.4a16.5 16.5 0 0 0 0 4zm.8 2h2.9c.3 1.3.8 2.5 1.4 3.6A8 8 0 0 1 5.1 16zM8 8H5.1a8 8 0 0 1 4.3-3.6C8.8 5.5 8.3 6.7 8 8zm4 12c-.8-1.2-1.5-2.5-1.9-4h3.8c-.4 1.5-1.1 2.8-1.9 4zm2.3-6H9.7a14.7 14.7 0 0 1 0-4h4.6a14.7 14.7 0 0 1 0 4zm.3 5.6c.6-1.1 1.1-2.3 1.4-3.6h2.9a8 8 0 0 1-4.3 3.6zm1.7-5.6a16.5 16.5 0 0 0 0-4h3.4a8 8 0 0 1 0 4z"/></svg>
          www.velvetatelier.com
        </li>
      </ul>
      <p class="address">18, Linden Court Avenue<br>20714, Westmere</p>
    </div>
  </section>
</body>
</html>
```